Global E-commerce Business Needs Banner Ad

We need banner ads for a fast growing E-commerce business cater mostly to women. The ads must have unique and beautiful background that accentuate the products. The ads should also have between 1-4 products in it. It needs to have the headline "Up To 80% Off Retail" in the ad. The ad also needs to have our logo and a "View Now" button. The ad should be more feminine and playful. Each product should have a different background design specially for the product to make it more beautiful.

Dimension: 320 by 480 pixel

Target Market(s)

Women

Industry/Entity Type

Business

Requirements
Must have
• 1) "Up To 80% Off Retail"
• 2) Brimvale Logo
• 3) "View Now" button

```html
<!DOCTYPE html>
<html lang="en">
<head>
<meta charset="utf-8">
<title>Brimvale – Up To 80% Off Retail</title>
<link rel="stylesheet" href="https://fonts.googleapis.com/css2?family=Arimo:wght@400;700&display=swap">
<style>
  :root {
    --purple-deep: #4a2183;
    --purple-mid: #6a3aa8;
    --purple-glow: #8d5ec9;
    --white: #ffffff;
    --ink: #1e1e1e;
    --pink: #e2197c;
    --pink-dark: #c10f66;
    --yellow: #ffea00;
    --peach: #ffb36b;
    --sky: #9fd4f2;
    --rose: #f7a1b9;
  }
  * { margin: 0; padding: 0; box-sizing: border-box; }
  html, body { width: 800px; height: 1200px; overflow: hidden; }
  body { font-family: "Arimo", Arial, sans-serif; background: var(--purple-deep); }

  .banner {
    position: relative;
    width: 800px; height: 1200px;
    overflow: hidden;
    background: radial-gradient(ellipse at 50% 55%, var(--purple-glow) 0%, var(--purple-mid) 45%, var(--purple-deep) 100%);
  }
  .header-curve { position: absolute; left: 0; top: 0; width: 800px; height: 180px; }

  .brand {
    position: absolute; left: 40px; top: 50px;
    display: flex; align-items: center; gap: 12px;
    font-size: 44px; font-weight: 400; color: var(--ink);
    letter-spacing: 1px;
  }
  .brand-mark { width: 22px; height: 22px; background: var(--ink); }

  .offer-badge {
    position: absolute; left: 455px; top: -95px;
    width: 350px; height: 350px; border-radius: 50%;
    background: radial-gradient(circle at 45% 55%, #f23d94 0%, var(--pink) 60%, var(--pink-dark) 100%);
    border: 8px solid var(--white);
    box-shadow: 0 6px 14px rgba(0,0,0,.35);
    color: var(--white); text-align: center;
    display: flex; flex-direction: column; justify-content: flex-end;
    padding-bottom: 62px;
  }
  .offer-badge .small { font-size: 48px; line-height: 1.05; }
  .offer-badge .big { font-size: 78px; font-weight: 700; color: var(--yellow); line-height: 1.05; }

  .product-card {
    position: absolute; left: 82px; width: 643px; height: 275px;
    box-shadow: 0 4px 10px rgba(0,0,0,.3);
  }
  .card-gold { top: 175px; background: linear-gradient(90deg, #ffffff 0%, #fff3e6 40%, var(--peach) 100%); }
  .card-sky  { top: 482px; background: linear-gradient(90deg, #ffffff 0%, #e3f3fc 40%, var(--sky) 100%); }
  .card-rose { top: 795px; background: linear-gradient(90deg, #ffffff 0%, #fde8ee 40%, var(--rose) 100%); }

  .product-photo { position: absolute; border-radius: 50%; }
  .card-gold .product-photo { left: 10px; top: 5px; width: 285px; height: 265px;
    background: radial-gradient(circle, #f2f2f2 0%, #d9b46a 55%, rgba(217,180,106,0) 72%); }
  .card-sky .product-photo { left: 395px; top: 15px; width: 240px; height: 245px;
    background: radial-gradient(circle, #8fc9ee 0%, #b9c0c8 40%, #e03a8e 58%, rgba(224,58,142,0) 72%); }
  .card-rose .product-photo { left: 15px; top: 10px; width: 300px; height: 255px;
    background: radial-gradient(circle, #f36ca5 0%, #2b2b2b 45%, #9a9a9a 58%, rgba(154,154,154,0) 72%); }

  .product-name { position: absolute; font-size: 46px; color: var(--ink); }
  .card-gold .product-name { left: 380px; top: 170px; }
  .card-sky  .product-name { left: 30px;  top: 195px; }
  .card-rose .product-name { left: 380px; top: 185px; }

  .discount-tag {
    position: absolute; top: 10px; width: 72px; height: 100px;
    background: var(--pink); color: var(--white);
    border-radius: 0 0 14px 0;
    text-align: center; font-size: 34px; line-height: 1;
    padding-top: 14px;
  }
  .card-sky .discount-tag { left: 18px; }
  .card-rose .discount-tag { right: 18px; top: 10px; border-radius: 0 0 0 14px; }
  .discount-tag sup { font-size: 18px; vertical-align: 12px; }
  .discount-tag .off { display: block; margin-top: 6px; }

  .cta-row {
    position: absolute; left: 0; top: 1107px; width: 800px; height: 63px;
    display: flex; align-items: center; justify-content: center; gap: 0;
  }
  .cta-rule { width: 95px; height: 3px; background: var(--white); margin: 0 62px; }
  .view-now {
    width: 290px; height: 63px;
    border: 3px solid var(--white);
    color: var(--yellow); font-size: 44px;
    display: flex; align-items: center; justify-content: center; gap: 12px;
    text-decoration: none;
  }
  .view-now svg { width: 34px; height: 22px; }
</style>
</head>
<body>
  <main class="banner">
    <svg class="header-curve" viewBox="0 0 800 180" aria-hidden="true">
      <path d="M0 0 H800 V90 C620 150 300 150 0 155 Z" fill="#ffffff"/>
    </svg>

    <div class="brand"><span class="brand-mark"></span>Brimvale</div>

    <div class="offer-badge">
      <span class="small">Up To</span>
      <span class="big">80% OFF</span>
      <span class="small">Retail</span>
    </div>

    <section class="product-card card-gold">
      <div class="product-photo" role="img" aria-label="Gold engagement ring with a large solitaire diamond and pavé band"></div>
      <p class="product-name">Name Here</p>
    </section>

    <section class="product-card card-sky">
      <div class="discount-tag">80<sup>%</sup><span class="off">OFF</span></div>
      <p class="product-name">Name Here</p>
      <div class="product-photo" role="img" aria-label="Silver ring set with blue and pink gemstones"></div>
    </section>

    <section class="product-card card-rose">
      <div class="product-photo" role="img" aria-label="Black gold bridal ring set with a pink centre stone"></div>
      <div class="discount-tag">80<sup>%</sup><span class="off">OFF</span></div>
      <p class="product-name">Name Here</p>
    </section>

    <div class="cta-row">
      <span class="cta-rule"></span>
      <a class="view-now" href="#">View Now
        <svg viewBox="0 0 34 22" aria-hidden="true">
          <path d="M2 11 C8 2 26 2 32 11 C26 20 8 20 2 11 Z" fill="none" stroke="#ffea00" stroke-width="2.5"/>
          <circle cx="17" cy="11" r="5" fill="#ffea00"/>
        </svg>
      </a>
      <span class="cta-rule"></span>
    </div>
  </main>
</body>
</html>
```